Become a Mentor - For Musicians, Artists, Producers and Teachers

Here is the full creative brief:

https://files.plenwick.com/sheets/d/4kTqpLm8Wz_2RNa7Hc3Xv91Jd0Gb5YeUsQ6fNo8rTpxa/view?mode=shared

Here is the background image file: https://www.trovecrate.com/sh/83jbwtrmq5dkx2u/BBHn4k7QTf2ZpLeXX-wr9MUHe?dl=0

LOGO:
https://www.trovecrate.com/sh/k472rufmpdo9b6w/BBKLe3RtHY5J-sFQnLZw7Ggma?dl=0

```html
<!DOCTYPE html>
<html lang="en">
<head>
<meta charset="utf-8">
<title>Become a Mentor Today</title>
<link href="https://fonts.googleapis.com/css2?family=Bebas+Neue&family=Kaushan+Script&family=Lato:wght@400;700&family=Oswald:wght@500;600&display=swap" rel="stylesheet">
<style>
  :root{
    --page:#f2f2f4;
    --navy-deep:#070a22;
    --navy:#161b4d;
    --navy-mid:#1f2766;
    --red:#c4080f;
    --red-dark:#7e0308;
    --white:#ffffff;
    --photo-warm:#8a7a6a;
    --photo-cool:#5c5f66;
  }
  *{margin:0;padding:0;box-sizing:border-box}
  html,body{width:1200px;height:830px;overflow:hidden;background:var(--page)}
  .poster{
    position:absolute;left:320px;top:19px;width:560px;height:792px;overflow:hidden;
    background:radial-gradient(ellipse at 50% 60%,var(--navy-mid) 0%,var(--navy) 45%,var(--navy-deep) 100%);
  }
  .headline{position:absolute;left:30px;top:24px;font-family:"Bebas Neue",sans-serif;line-height:.85;color:var(--white)}
  .headline__lead{display:block;font-size:42px;letter-spacing:1px}
  .headline__main{display:block;font-size:102px;letter-spacing:1px;
    background:linear-gradient(180deg,#fff 0%,#e6e8ee 45%,#9ea3ad 55%,#fff 100%);
    -webkit-background-clip:text;background-clip:text;color:transparent}
  .brand{position:absolute;left:374px;top:40px;display:flex;align-items:center;gap:8px}
  .brand__dot{width:14px;height:14px;border-radius:50%;background:var(--white)}
  .brand__name{font-family:"Lato",sans-serif;font-weight:700;font-size:15px;line-height:1.15;color:var(--white);letter-spacing:1px;text-transform:uppercase}
  .photo{position:absolute;left:0;top:150px;width:560px;height:340px;
    background:linear-gradient(100deg,var(--photo-warm) 0%,#a79d93 35%,#8f8f92 60%,var(--photo-cool) 100%)}
  .band{position:absolute;left:0;top:0}
  .mentor{position:absolute;z-index:1;left:30px;top:462px;font-family:"Bebas Neue",sans-serif;font-size:104px;line-height:1;letter-spacing:1px;
    transform:rotate(-5deg);transform-origin:left bottom;
    background:linear-gradient(180deg,#fff 0%,#eef0f3 48%,#a7abb4 56%,#fff 100%);
    -webkit-background-clip:text;background-clip:text;color:transparent;
    filter:drop-shadow(0 3px 2px rgba(0,0,0,.55))}
  .become{position:absolute;z-index:2;left:176px;top:384px;font-family:"Kaushan Script",cursive;font-size:50px;line-height:1;color:var(--white);transform:rotate(-7deg);text-shadow:0 2px 4px rgba(0,0,0,.6)}
  .intro{position:absolute;left:0;width:560px;top:574px;text-align:center;font-family:"Lato",sans-serif}
  .intro__line{font-size:14px;color:var(--white)}
  .intro__for{font-size:14px;color:var(--red);margin-top:4px}
  .roles{position:absolute;left:0;top:620px;width:560px;list-style:none}
  .role{position:absolute;width:120px;margin-left:-60px;text-align:center}
  .role__icon{display:block;margin:0 auto;width:20px;height:38px;background:var(--red);border-radius:10px 10px 3px 3px}
  .role__label{display:block;margin-top:12px;font-family:"Lato",sans-serif;font-weight:700;font-size:15px;color:var(--white)}
  .apply{position:absolute;left:180px;top:697px;width:198px;height:47px;border:2px solid var(--white);border-radius:6px;
    background:linear-gradient(180deg,#ee1a22 0%,var(--red) 50%,var(--red-dark) 100%);
    font-family:"Oswald",sans-serif;font-weight:600;font-style:italic;font-size:30px;color:var(--white);
    text-align:center;line-height:42px;letter-spacing:.5px;text-shadow:0 2px 2px rgba(0,0,0,.5)}
  .contact{position:absolute;left:0;width:560px;top:756px;text-align:center;font-family:"Oswald",sans-serif;font-weight:500;font-size:17.5px;color:var(--white)}
  .contact__or{color:var(--red)}
</style>
</head>
<body>
  <main class="poster">
    <h1 class="headline"><span class="headline__lead">Start your</span><span class="headline__main">Career</span></h1>

    <div class="brand">
      <span class="brand__dot"></span>
      <span class="brand__name">Meridian<br>School of Music</span>
    </div>

    <div class="photo" role="img" aria-label="Two young men talking in a music studio beside a mixing desk and speakers"></div>

    <svg class="band" width="560" height="792" viewBox="0 0 560 792" aria-hidden="true">
      <defs>
        <linearGradient id="bandRed" x1="0" y1="0" x2="0" y2="1">
          <stop offset="0" stop-color="#d9101a"/>
          <stop offset="1" stop-color="#8e0409"/>
        </linearGradient>
      </defs>
      <polygon points="0,140 560,130 560,162 0,172" fill="#0b0e2a"/>
      <polygon points="0,470 560,480 560,560 0,570" fill="#10143d"/>
      <polygon points="0,475 560,420 560,535 0,555" fill="url(#bandRed)"/>
    </svg>

    <p class="mentor">Mentor Today</p>
    <p class="become">Become a</p>

    <div class="intro">
      <p class="intro__line">Turn your skills and passion for music into a career</p>
      <p class="intro__for">Designed for -</p>
    </div>

    <ul class="roles">
      <li class="role" style="left:101px"><span class="role__icon" role="img" aria-label="Musician figure"></span><span class="role__label">MUSICIANS</span></li>
      <li class="role" style="left:215px"><span class="role__icon" role="img" aria-label="Artist figure"></span><span class="role__label">ARTISTS</span></li>
      <li class="role" style="left:334px"><span class="role__icon" role="img" aria-label="Producer figure"></span><span class="role__label">PRODUCERS</span></li>
      <li class="role" style="left:461px"><span class="role__icon" role="img" aria-label="Teacher figure"></span><span class="role__label">TEACHERS</span></li>
    </ul>

    <div class="apply">APPLY NOW</div>

    <p class="contact">CALL 1300 555 014 <span class="contact__or">OR</span> WWW.MERIDIANSCHOOLOFMUSIC.COM.AU</p>
  </main>
</body>
</html>
```